Drillvane Business Card Design Project

We need a business card design for a new company called "Drillvane Systems". Drillvane provides 3D visualization software for subsurface oil and gas data so you can make confident downhole decisions.

Our goal is to provide easy to understand big pictures of your data so your can make confident planning decisions.

Our tagline is
SEAMLESS DATA SHARING. EFFECTIVE COLLABORATION. CONFIDENT DECISION-MAKING

Check out http://www.drillvane-example.com for more ideas.

The design should promote a technology company that delivers web-based solutions focused on photo-realistic 3D graphics.

The colors from our existing logo (attached) are one option but not a requirement. The design SHOULD NOT use the existing logo.

The design should be two sided and full color. If you require any special print considerations (example: paper type, matte finish, metallic ink, etc) please provide detailed comments. Please also specify any desired details such as rounding of corners, etc.

IF YOU USE BLACK our printer states "We recommend using CMYK black (0, 0, 0, 100) or for a rich black (60, 40, 40, 100). Ensure your artwork is in CMYK mode before adjusting the black."

For design purposes you can use the following contact information

name: Marcus Pell
title: founder
phone: 555.987.6543
email: marcus@drillvane-example.com

company information
Drillvane is our "branded" name
"Drillvane Systems" is our official name
www.drillvane-example.com

address:
Suite 210
482 Larkin Avenue SW
Calgary, AB, Canada
T3K 4R8

Target Market(s)

Companies spend a lot of time collecting, organizing and analyzing data but it's really hard to to get a big picture view of current and planned projects, especially in context to existing wellbores, geology and downhole equipment

Drillvane enables you to explore the big picture in an immersive, 3D environment. Our goal is to help transform you rich data into an easily understood picture, to make confident planning decisions and anticipate trouble events before the expensive execution phase.

Industry/Entity Type

Oil And Gas

Requirements
Must have
• The business card design should be sized to a standard 3.5 x 2 inches and print ready. See the attachment for a sample sized card
It MUST meet these requirements:
Exported as PDF file with two pages:
page 1: front design
page 2: back design
All Images must be 300ppi or higher (at 100%)
CMYK colour mode
0.125 inches of bleed on all sides (0.25 inches additional width and height)
0.125 inch safety margin (inside trim line)

```html
<!DOCTYPE html>
<html lang="en">
<head>
<meta charset="utf-8">
<title>Drillvane Systems — Business Card</title>
<link rel="stylesheet" href="https://fonts.googleapis.com/css2?family=Questrial&family=Arimo:wght@400;700&display=swap">
<style>
  :root {
    --page-bg: #e4e1de;
    --card-white: #ffffff;
    --card-off: #f6f6f6;
    --back-field: #ebebeb;
    --brand-green: #8dc63f;
    --brand-grey: #5e5e5e;
    --ink: #2b2b2b;
    --ink-soft: #3c3c3c;
    --shadow: rgba(0, 0, 0, 0.28);
  }
  * { box-sizing: border-box; margin: 0; padding: 0; }
  html, body {
    width: 1000px;
    height: 1200px;
    overflow: hidden;
    background: var(--page-bg);
  }
  .card {
    position: absolute;
    left: 123px;
    width: 749px;
    height: 427px;
    overflow: hidden;
    box-shadow: 0 3px 10px var(--shadow);
  }

  /* Front */
  .card--front {
    top: 134px;
    background: linear-gradient(180deg, var(--card-white) 0%, var(--card-off) 100%);
  }
  .brand-lockup {
    position: absolute;
    top: 190px;
    left: 0;
    width: 100%;
    display: flex;
    flex-direction: column;
    align-items: center;
  }
  .brand-row {
    display: flex;
    align-items: center;
    gap: 16px;
  }
  .brand-square {
    width: 50px;
    height: 50px;
    background: var(--brand-green);
  }
  .brand-name {
    font-family: "Questrial", sans-serif;
    font-size: 68px;
    line-height: 1;
    color: var(--brand-grey);
  }
  .card-strapline {
    position: absolute;
    top: 292px;
    left: 0;
    width: 100%;
    text-align: center;
    font-family: "Questrial", sans-serif;
    font-size: 13px;
    letter-spacing: 2.4px;
    color: var(--brand-grey);
  }
  .contact-band {
    position: absolute;
    left: 0;
    bottom: 0;
    width: 100%;
    height: 69px;
    padding: 0 46px 0 48px;
    display: flex;
    align-items: center;
    justify-content: space-between;
    background: linear-gradient(180deg, #efefef 0%, #ffffff 45%, #ffffff 100%);
    box-shadow: inset 0 6px 8px -6px rgba(0, 0, 0, 0.12);
    font-family: "Questrial", sans-serif;
    font-size: 11px;
    letter-spacing: 1.6px;
    text-transform: uppercase;
    color: var(--ink);
  }

  /* Back */
  .card--back {
    top: 637px;
    background: var(--back-field);
  }
  .back-header {
    position: absolute;
    top: 0;
    left: 0;
    width: 100%;
    height: 118px;
    display: flex;
    align-items: center;
    justify-content: center;
    gap: 12px;
    background: linear-gradient(180deg, #ffffff 0%, #f7f7f7 100%);
    box-shadow: 0 3px 6px rgba(0, 0, 0, 0.18);
  }
  .back-header__dot {
    width: 22px;
    height: 22px;
    border-radius: 50%;
    background: var(--brand-green);
  }
  .back-header__name {
    font-family: "Questrial", sans-serif;
    font-size: 40px;
    line-height: 1;
    color: var(--brand-grey);
  }
  .person, .address {
    position: absolute;
    font-family: "Arimo", sans-serif;
    font-size: 14px;
    line-height: 22px;
    color: var(--ink-soft);
  }
  .person { top: 300px; left: 52px; }
  .address { top: 308px; left: 495px; }
  .person__name {
    font-size: 25px;
    font-weight: 700;
    line-height: 30px;
    color: var(--ink);
  }
  .person__name .surname { color: var(--brand-green); }
  .label { font-weight: 700; }
</style>
</head>
<body>

  <section class="card card--front" aria-label="Card front">
    <div class="brand-lockup">
      <div class="brand-row">
        <span class="brand-square"></span>
        <span class="brand-name">Drillvane</span>
      </div>
    </div>
    <p class="card-strapline">3D SUBSURFACE VISUALIZATION</p>
    <div class="contact-band">
      <span class="contact-band__site">Site: www.drillvane-example.com</span>
      <span class="contact-band__email">Email: marcus@drillvane-example.com</span>
    </div>
  </section>

  <section class="card card--back" aria-label="Card back">
    <header class="back-header">
      <span class="back-header__dot"></span>
      <span class="back-header__name">Drillvane Systems</span>
    </header>
    <div class="person">
      <p class="person__name">Marcus <span class="surname">Pell</span></p>
      <p class="label">Founder</p>
      <p>Phone: 555.987.6543</p>
      <p>email: marcus@drillvane-example.com</p>
    </div>
    <div class="address">
      <p class="label">Address:</p>
      <p>Suite 210, 482 Larkin Avenue SW</p>
      <p>Calgary, AB, Canada</p>
      <p>T3K 4R8</p>
    </div>
  </section>

</body>
</html>
```